Health/Nutrition/Fitness Graphic needed urgently!

I am looking for a graphic that introduces the concept of health, nutrition and exercise working together to create optimum performance. It needs to exude energy and be clear. It is for a new business called "Vortal" that combines healthcare, nutrition services and fitness training to give clients the best success they can get and will be used in pitch documents, advertising and on the website. The example attached is linear - the winning graphic will need to show each element working together so please do not submit linear graphics. This is NOT a logo, but is a graphic illustrating a concept

Target Market(s)

Clients looking for a transformation in their health and fitness

Industry/Entity Type

Health And Wellness

Font styles to use
Sans Serif

Requirements
Must have
• the 3 elements of health, nutrition and excercise/fitness working together. modern, energetic and clean. What is crucial to show is that these elements work together to leverage effort and enhance/ maximise results.
Should not have
• This is NOT a logo for Vortal and there should be no text in the graphic unless (Health, Fitness and Nutrition are the words used). This is a graphic design used to illustrate a concept only.

```html
<!DOCTYPE html>
<html lang="en">
<head>
<meta charset="utf-8">
<title>Vortal – Health, Nutrition, Exercise</title>
<link rel="stylesheet" href="https://fonts.googleapis.com/css2?family=Exo+2:wght@300;400;600&display=swap">
<style>
  :root {
    --bg: #ffffff;
    --health: #5fba4b;
    --health-soft: #b2dda0;
    --nutrition: #f7941d;
    --nutrition-soft: #fbc78c;
    --exercise: #21c1f1;
    --exercise-soft: #a4dff6;
    --label: #707070;
    --centre-label: #6a6a6a;
    --leader: #9c9c9c;
    --icon-area: rgba(255, 255, 255, 0.4);
  }
  html, body {
    margin: 0;
    padding: 0;
    width: 1200px;
    height: 846px;
    overflow: hidden;
    background: var(--bg);
  }
  .canvas {
    position: relative;
    width: 1200px;
    height: 846px;
  }
  .concept-wheel {
    display: block;
    width: 1200px;
    height: 846px;
  }
  .segment-health { fill: var(--health); }
  .segment-nutrition { fill: var(--nutrition); }
  .segment-exercise { fill: var(--exercise); }
  .ring-health { fill: var(--health-soft); }
  .ring-nutrition { fill: var(--nutrition-soft); }
  .ring-exercise { fill: var(--exercise-soft); }
  .hub { fill: var(--bg); }
  .divider { stroke: var(--bg); stroke-width: 6; }
  .icon-area { fill: var(--icon-area); }
  .leader { fill: none; stroke: var(--leader); stroke-width: 1; }
  .leader-dot, .leader-head { fill: var(--leader); }
  .pillar-label {
    font-family: "Exo 2", sans-serif;
    font-weight: 300;
    font-size: 18px;
    fill: var(--label);
  }
  .hub-label {
    font-family: "Exo 2", sans-serif;
    font-weight: 600;
    font-size: 16px;
    fill: var(--centre-label);
  }
</style>
</head>
<body>
<main class="canvas">
  <svg class="concept-wheel" viewBox="0 0 850 600" preserveAspectRatio="xMidYMid meet" xmlns="http://www.w3.org/2000/svg">
    <!-- outer segments -->
    <path class="segment-health" d="M428 149 A153 153 0 0 0 295.5 378.5 L360.5 341 A78 78 0 0 1 428 224 Z"/>
    <path class="segment-nutrition" d="M428 149 A153 153 0 0 1 560.5 378.5 L495.5 341 A78 78 0 0 0 428 224 Z"/>
    <path class="segment-exercise" d="M560.5 378.5 A153 153 0 0 1 295.5 378.5 L360.5 341 A78 78 0 0 0 495.5 341 Z"/>

    <!-- inner soft ring -->
    <path class="ring-health" d="M428 302 L428 224 A78 78 0 0 0 360.5 341 Z"/>
    <path class="ring-nutrition" d="M428 302 L428 224 A78 78 0 0 1 495.5 341 Z"/>
    <path class="ring-exercise" d="M428 302 L495.5 341 A78 78 0 0 1 360.5 341 Z"/>

    <!-- dividers between pillars -->
    <line class="divider" x1="428" y1="302" x2="428" y2="140"/>
    <line class="divider" x1="428" y1="302" x2="568.3" y2="383"/>
    <line class="divider" x1="428" y1="302" x2="287.7" y2="383"/>

    <!-- hub -->
    <circle class="hub" cx="428" cy="302" r="64"/>
    <text class="hub-label" x="428" y="308" text-anchor="middle">Vortal</text>

    <!-- pillar icon areas -->
    <rect class="icon-area" x="303" y="224" width="42" height="67" rx="8" role="img" aria-label="Icon of a person with arms raised, representing health"/>
    <rect class="icon-area" x="512" y="226" width="44" height="55" rx="14" role="img" aria-label="Apple icon, representing nutrition"/>
    <rect class="icon-area" x="408" y="387" width="47" height="60" rx="8" role="img" aria-label="Icon of a person stretching, representing exercise"/>

    <!-- Health leader -->
    <circle class="leader-dot" cx="293" cy="208" r="2.5"/>
    <polyline class="leader" points="293,208 280,175 238,175"/>
    <path class="leader-head" d="M233 175 L239 172.5 L239 177.5 Z"/>
    <text class="pillar-label" x="222" y="180" text-anchor="end">Health</text>

    <!-- Nutrition leader -->
    <circle class="leader-dot" cx="562" cy="208" r="2.5"/>
    <polyline class="leader" points="562,208 576,175 618,175"/>
    <path class="leader-head" d="M623 175 L617 172.5 L617 177.5 Z"/>
    <text class="pillar-label" x="632" y="180">Nutrition</text>

    <!-- Exercise leader -->
    <circle class="leader-dot" cx="428" cy="467" r="2.5"/>
    <line class="leader" x1="428" y1="467" x2="428" y2="509"/>
    <path class="leader-head" d="M428 514 L425.5 508 L430.5 508 Z"/>
    <text class="pillar-label" x="428" y="534" text-anchor="middle">Exercise</text>
  </svg>
</main>
</body>
</html>
```